Layout für Longboardshop
Zielgruppe
Online Shop für Longboards, basierend auf Ladenwerk 4.1.2
Zielgruppe: Sportliche Menschen mit Hang zum Wellenreiten, Surfen,Kiten, Snowboarden oder Skateboarden.
Aufgabenstellung
Erstellung des Grunddesigns (Header, Footer, Menü, Detailansicht, Buttons) als PSD. Die Umsetzung in ein Template erledigen wir alleine.
Neugründung: Es existieren noch keine Logos oder Farbvorgaben.
We have no site, it is a completly new project. There are no limits concerning colors, fonts etc.
Competitors:
http://www.brettfahrer-welt.de
http://wilhelmine-bretter.de/
http://www.rollbrettladen.de/
http://www.kavero.de/de_DE/Skateboard/Longboards.html?sid=1
http://www.pirumo-bretter.de/
I think, big pictures transporting the surfstyle attitude of this sport works good.
Der Grundaufbau sollte sich an http://www.ladenwerkdemo.de/ anlehnen, um den Anpassungsaufwand mgl. überschaubar zu halten.

```html
<!DOCTYPE html>
<html lang="de">
<head>
<meta charset="utf-8">
<title>brettmarkt.de – Longboard Shop</title>
<link href="https://fonts.googleapis.com/css2?family=Source+Sans+3:wght@300;400;600;700&display=swap" rel="stylesheet">
<style>
:root{
  --blue:#1a95c4;
  --blue-dark:#0d77a3;
  --ink:#333;
  --dark:#353535;
  --page:#ececec;
  --panel:#d6d6d6;
  --white:#fff;
  --line:#dcdcdc;
  --orange:#e28a00;
  --link:#1d7fb8;
}
*{box-sizing:border-box;margin:0;padding:0}
html,body{width:1200px;height:1200px;overflow:hidden}
body{font-family:"Source Sans 3",sans-serif;background:var(--page);color:var(--ink);position:relative;font-size:8px}
.abs{position:absolute}
svg{display:block}
.topbar{left:0;top:0;width:1200px;height:24px;background:var(--dark);color:#ddd;font-size:7px}
.topbar .item{position:absolute;top:0;height:24px;display:flex;align-items:center;gap:8px;border-left:1px solid #4a4a4a;padding-left:11px}
.search{position:absolute;left:827px;top:4px;width:119px;height:16px;background:#fff;border-radius:2px;color:#999;font-size:6.5px;padding:4px 5px}
.search svg{position:absolute;right:4px;top:4px}
.flag{width:13px;height:8px;background:linear-gradient(#222 33%,#d00 33% 66%,#fc0 66%)}
.brand{left:480px;top:52px;width:240px;text-align:center;font-size:44px;font-weight:700;color:#111;letter-spacing:-1px}
.cart{left:797px;top:54px;width:163px;height:52px;background:#fff;border:3px solid #e2e2e2;padding:5px 10px;font-size:6.5px}
.cart .t{font-weight:700;font-size:8px;color:#333}
.cart .r{display:flex;justify-content:space-between;width:100px}
.cart .bag{position:absolute;right:12px;top:5px}
.cart .sel{margin-top:3px;width:98px;height:12px;border:1px solid #ddd;color:#777;padding:1px 4px}
.nav{left:240px;top:136px;width:720px;height:23px;background:linear-gradient(var(--blue),var(--blue-dark));display:flex;color:#fff;font-weight:600;font-size:8px}
.nav div{display:flex;align-items:center;justify-content:center;gap:8px;border-right:1px solid #0b6a92}
.nav .home{background:#fff;color:var(--blue-dark);margin-left:10px;margin-top:-3px;height:26px}
.stage{left:240px;top:159px;width:720px;height:282px;background:#fff}
.hero{left:247px;top:176px;width:706px;height:258px;background:linear-gradient(#6e88c4 0%,#a7b3c7 35%,#f2b45a 60%,#e0801f 78%,#3b2a1e 100%)}
.hero-copy{left:270px;top:204px;color:#fff;line-height:.95}
.hero-copy .l1{font-weight:300;font-size:26px}
.hero-copy .l2{font-weight:700;font-size:26px}
.hero-copy .l3{margin-top:8px;padding:4px 1px;border-top:1px solid rgba(255,255,255,.6);border-bottom:1px solid rgba(255,255,255,.6);font-size:17px;font-weight:300;width:151px;white-space:nowrap}
.hero-copy b{font-weight:700}
.side{left:240px;top:470px;width:169px;height:485px;background:var(--panel);padding:5px 6px}
.head{height:22px;background:linear-gradient(var(--blue),var(--blue-dark));color:#fff;font-weight:600;font-size:8.5px;display:flex;align-items:center;justify-content:center;margin-bottom:4px}
.opt{height:24px;background:#fff;border-bottom:1px solid var(--line);display:flex;align-items:center;padding-left:22px;gap:12px;font-size:8px;color:#555}
.opt .cb{width:10px;height:10px;border:1px solid #ccc;border-radius:2px;background:#f5f5f5;font-size:8px;line-height:9px;text-align:center;color:var(--blue-dark)}
.opt.on{font-size:10px;font-weight:600;color:#222}
.price{height:72px;background:#fff;margin-bottom:5px;position:relative;font-size:7.5px}
.price .bar{position:absolute;left:17px;top:34px;width:118px;height:2px;background:#444}
.price span{position:absolute}
.reset{left:240px;top:968px;width:51px;height:30px;background:#4a4a4a}
.go{left:297px;top:968px;width:112px;height:30px;background:linear-gradient(var(--blue),var(--blue-dark));color:#fff;font-weight:600;font-size:8.5px;display:flex;align-items:center;justify-content:center;gap:6px}
.grid{left:420px;top:470px;width:540px;height:528px;background:var(--panel)}
.card{position:absolute;width:122px;height:216px;background:#fff;border:1px solid #ccc;padding:5px 4px;text-align:center}
.card .img{height:139px;border:1px solid #ccc;margin:0 1px 10px}
.card .nm{font-size:7px;color:#333}
.card .nm a{color:var(--link)}
.card p{font-size:7.3px;text-align:justify;text-align-last:left;line-height:1.45;color:#222;margin-top:1px;white-space:nowrap}
.card p a{color:var(--link)}
.card .btns{display:flex;gap:3px;margin-top:6px;font-size:6.5px;font-weight:600}
.card .d{background:#4a4a4a;color:#ddd;padding:5px 4px;font-weight:400}
.card .w{flex:1;background:var(--blue);color:#fff;padding:5px 0}
.new{position:absolute;left:-1px;top:-1px;width:32px;height:32px;overflow:hidden}
.new span{position:absolute;left:-14px;top:7px;width:50px;height:9px;background:#d21f1f;color:#fff;font-size:5.5px;font-weight:700;line-height:9px;text-align:center;transform:rotate(-45deg)}
.pg{top:964px;width:24px;height:22px;background:#fff;display:flex;align-items:center;justify-content:center}
.foot{left:0;top:1037px;width:1200px;height:139px;background:var(--dark);border-top:2px solid var(--blue);color:#ddd;font-size:8px}
.foot h4{font-weight:400;font-size:8.5px;color:#fff}
.foot h4 span{color:var(--blue)}
.tags{margin-top:13px;margin-left:-5px}
.tags .row{display:flex;gap:9px;margin-bottom:5px}
.tags span{background:#4a4a4a;padding:3px 4px;font-size:8px}
.tags .on{background:var(--blue-dark);color:#fff}
.foot .col{position:absolute;top:20px}
.foot a{color:var(--blue)}
.pay{display:flex;gap:10px;margin-top:8px}
.pay span{width:44px;height:21px;background:#fff;color:#1d5c9a;font-size:6px;font-weight:600;display:flex;align-items:center;justify-content:center}
.copy{left:0;top:1176px;width:1200px;height:24px;background:var(--blue-dark);color:#e6f3f9;font-size:7.5px;text-align:center;line-height:24px}
</style>
</head>
<body>
<div class="abs topbar">
  <div class="item" style="left:469px;width:83px"><svg width="10" height="9" viewBox="0 0 10 9"><circle cx="5" cy="2.5" r="2.3" fill="#ccc"/><path d="M0.5 9c0-3 2-4.3 4.5-4.3S9.5 6 9.5 9z" fill="#ccc"/></svg>Mein Konto</div>
  <div class="item" style="left:552px;width:77px"><svg width="9" height="11" viewBox="0 0 9 11"><rect x=".7" y="1.5" width="7.6" height="9" rx="1" fill="none" stroke="#ccc" stroke-width="1.2"/><rect x="2.7" y=".3" width="3.6" height="2.2" fill="#ccc"/><path d="M2.5 6.5l1.5 1.5 2.5-3" fill="none" stroke="#ccc" stroke-width="1"/></svg>Merkzettel</div>
  <div class="item" style="left:629px;width:82px"><svg width="10" height="10" viewBox="0 0 10 10"><path d="M1 1l8 8M9 1L1 9" stroke="#ccc" stroke-width="1.6" stroke-linecap="round"/></svg>Service/Hilfe</div>
  <div class="item" style="left:711px;width:53px"><svg width="7" height="5" viewBox="0 0 7 5"><path d="M.5 .8l3 3 3-3" fill="none" stroke="#ccc" stroke-width="1.4"/></svg>EUR</div>
  <div class="item" style="left:764px;width:48px"><svg width="7" height="5" viewBox="0 0 7 5"><path d="M.5 .8l3 3 3-3" fill="none" stroke="#ccc" stroke-width="1.4"/></svg><span class="flag"></span></div>
  <div class="search">Suchbegriff eingeben<svg width="8" height="8" viewBox="0 0 8 8"><circle cx="4.8" cy="3.2" r="2.3" fill="none" stroke="#666"/><path d="M3.2 4.8L.8 7.2" stroke="#666" stroke-width="1.2"/></svg></div>
</div>

<div class="abs brand">brettmarkt.de</div>

<div class="abs cart">
  <div class="r"><span class="t">WARENKORB</span><span style="color:#d33">0,00 €*</span></div>
  <div class="r" style="color:var(--orange)"><span>Bonuspunkte:</span><span>0</span></div>
  <div class="sel">Positionen anzeigen ⌄</div>
  <svg class="bag" width="20" height="30" viewBox="0 0 20 30"><path d="M6 8V5a4 4 0 0 1 8 0v3" fill="none" stroke="#1a7fa8" stroke-width="1.3"/><path d="M2 8h16l1.5 21H.5z" fill="#2a9fcc"/></svg>
</div>

<nav class="abs nav">
  <div class="home" style="width:88px"><svg width="12" height="11" viewBox="0 0 12 11"><path d="M6 .5L.5 5.5h1.8V10.5h3V7.5h1.4v3h3V5.5h1.8z" fill="#0d77a3"/></svg>HOME</div>
  <div style="width:135px"><svg width="38" height="10" viewBox="0 0 38 10"><rect x="4" y="1.5" width="30" height="7" rx="3.5" fill="#fff"/><rect x=".5" y="3.5" width="4" height="3" rx="1" fill="#fff"/><rect x="33.5" y="3.5" width="4" height="3" rx="1" fill="#fff"/></svg>DECKS</div>
  <div style="width:103px"><svg width="11" height="11" viewBox="0 0 11 11"><path d="M.5 .5h10v2.4H6.8V10.5H4.2V2.9H.5z" fill="#fff"/></svg>ZUBEHÖR</div>
  <div style="width:82px"><span style="font-size:11px;font-weight:700">%</span>SALE</div>
  <div style="width:93px"><svg width="19" height="11" viewBox="0 0 19 11"><circle cx="5" cy="3" r="2.2" fill="#fff"/><circle cx="14" cy="3" r="2.2" fill="#fff"/><circle cx="9.5" cy="3.6" r="2.6" fill="#fff"/><path d="M4 11c0-3.5 2.5-5 5.5-5S15 7.5 15 11z" fill="#fff"/><path d="M.5 10c0-2.6 1.8-3.8 4.5-3.8L4 10zM18.5 10c0-2.6-1.8-3.8-4.5-3.8l1 3.8z" fill="#fff"/></svg>TEAM</div>
  <div style="width:91px"><svg width="13" height="12" viewBox="0 0 13 12"><rect x=".7" y="2.5" width="10" height="8.5" fill="none" stroke="#fff" stroke-width="1.2"/><path d="M2.5 1h10v8" fill="none" stroke="#fff" stroke-width="1"/><path d="M2 10l3-3.5 2 2 1.5-1.5L10 10z" fill="#fff"/></svg>BILDER</div>
  <div style="width:118px;border:0"><svg width="15" height="10" viewBox="0 0 15 10"><rect x=".5" y=".5" width="14" height="9" fill="#fff"/><path d="M.8 .8l6.7 5 6.7-5" fill="none" stroke="#0d77a3" stroke-width="1"/></svg>KONTAKT</div>
</nav>

<div class="abs stage"></div>
<div class="abs hero" role="img" aria-label="Foto: Longboarder steht bei Sonnenuntergang auf einem Felsen über einem Tal"></div>
<div class="abs hero-copy">
  <div class="l1">DIE NEUSTEN</div>
  <div class="l2">REDUZIERTEN</div>
  <div class="l2">ARTIKEL <span style="font-size:16px;margin-left:30px">»</span></div>
  <div class="l3">BIS ZUM <b>28.10.2013</b></div>
</div>

<aside class="abs side">
  <div class="head">MARKE</div>
  <div class="opt"><span class="cb"></span>Auswahl #1</div>
  <div class="opt on"><span class="cb">✓</span>Auswahl #2</div>
  <div class="opt"><span class="cb"></span>Auswahl #3</div>
  <div class="opt"><span class="cb"></span>Auswahl #4</div>
  <div class="opt"><span class="cb"></span>Auswahl #5</div>
  <div class="opt"><span class="cb"></span>Auswahl #6</div>
  <div class="opt"><span class="cb"></span>Auswahl #7</div>
  <div class="opt"><span class="cb"></span>Auswahl #8</div>
  <div class="opt" style="margin-bottom:5px"><span class="cb"></span>Alle</div>
  <div class="head">PREISKLASSE</div>
  <div class="price">
    <span style="left:40px;top:16px">100€</span><span style="left:98px;top:15px">200€</span>
    <div class="bar"></div>
    <span style="left:70px;top:30px;width:8px;height:8px;border-radius:50%;background:#fff;border:1px solid #999"></span>
    <span style="left:9px;top:43px">&lt;50€</span>
    <span style="left:69px;top:41px;font-weight:700;font-size:10px">150€</span>
    <span style="left:125px;top:43px">250€&lt;</span>
  </div>
  <div class="head">ZUBEHÖR</div>
  <div class="opt"><span class="cb"></span>Auswahl #1</div>
  <div class="opt on"><span class="cb">✓</span>Auswahl #2</div>
  <div class="opt"><span class="cb"></span>Auswahl #3</div>
  <div class="opt"><span class="cb"></span>Auswahl #4</div>
</aside>
<div class="abs reset"><svg width="51" height="30"><circle cx="25.5" cy="15" r="6" fill="none" stroke="#fff" stroke-width="2" stroke-dasharray="30 8"/></svg></div>
<div class="abs go">FILTER STARTEN <svg width="12" height="9" viewBox="0 0 12 9"><path d="M1 .8l3.7 3.7L1 8.2M6 .8l3.7 3.7L6 8.2" fill="none" stroke="#fff" stroke-width="1.8"/></svg></div>

<section class="abs grid">
  <div class="card" style="left:7px;top:5px"><div class="img" role="img" aria-label="Produktfoto: zwei Longboard-Decks, schwarz und bunt" style="background:radial-gradient(ellipse 40% 45% at 50% 50%,#6e8598,#fff)"></div><div class="nm"><a>KIELWIND</a> | 123,00 €</div><p>Lorem Ipsum. Proin gravidanv<br>el velit auctor aliquet... <a>mehr</a></p><div class="btns"><span class="d">DETAILS</span><span class="w">IN DEN WARENKORB</span></div></div>
  <div class="card" style="left:141px;top:5px"><div class="img" role="img" aria-label="Produktfoto: zwei Holz-Longboards" style="background:radial-gradient(ellipse 40% 45% at 50% 50%,#c7a06d,#fff)"></div><div class="nm"><a>ZENITRA</a> | 92,00 €</div><p>Lorem Ipsum. Proin gravidanv<br>el velit auctor aliquet... <a>mehr</a></p><div class="btns"><span class="d">DETAILS</span><span class="w">IN DEN WARENKORB</span></div></div>
  <div class="card" style="left:276px;top:5px"><div class="img" role="img" aria-label="Produktfoto: grauer Skatehelm" style="background:radial-gradient(ellipse 42% 38% at 50% 45%,#a3a3a3,#fff)"></div><div class="nm"><a>KVL</a> | 41,00 €</div><p>Lorem Ipsum. Proin gravidanv<br>el velit auctor aliquet... <a>mehr</a></p><div class="btns"><span class="d">DETAILS</span><span class="w">IN DEN WARENKORB</span></div></div>
  <div class="card" style="left:411px;top:5px"><div class="img" role="img" aria-label="Produktfoto: zwei Longboards in Grün, Gelb und Rot" style="border-color:var(--blue);background:radial-gradient(ellipse 40% 45% at 50% 50%,#d8b640,#fff)"></div><div class="nm"><a>VOLANT</a> | 189,50 €</div><p style="font-weight:600">Lorem Ipsum. Proin gravidanv<br>el velit auctor aliquet... <a>mehr</a></p><div class="btns"><span class="d">DETAILS</span><span class="w">IN DEN WARENKORB</span></div></div>

  <div class="card" style="left:7px;top:261px"><div class="img" role="img" aria-label="Produktfoto: Longboard-Achse" style="background:radial-gradient(ellipse 45% 25% at 50% 45%,#b5b5b5,#fff)"></div><div class="nm"><a>LUTETIA</a> | 27,90 €</div><p>Lorem Ipsum. Proin gravidanv<br>el velit auctor aliquet... <a>mehr</a></p><div class="btns"><span class="d">DETAILS</span><span class="w">IN DEN WARENKORB</span></div></div>
  <div class="card" style="left:141px;top:261px"><div class="img" role="img" aria-label="Produktfoto: Kugellager" style="background:radial-gradient(ellipse 45% 38% at 50% 50%,#4a5560,#fff)"></div><div class="nm"><a>KUGEL 7</a> | 19,30 €</div><p>Lorem Ipsum. Proin gravidanv<br>el velit auctor aliquet... <a>mehr</a></p><div class="btns"><span class="d">DETAILS</span><span class="w">IN DEN WARENKORB</span></div></div>
  <div class="card" style="left:276px;top:261px"><div class="img" role="img" aria-label="Produktfoto: zwei dunkle Longboard-Decks" style="background:radial-gradient(ellipse 40% 45% at 50% 50%,#5a5040,#fff)"></div><div class="new"><span>NEU</span></div><div class="nm"><a>MARENO</a> | 103,50 €</div><p>Lorem Ipsum. Proin gravidanv<br>el velit auctor aliquet... <a>mehr</a></p><div class="btns"><span class="d">DETAILS</span><span class="w">IN DEN WARENKORB</span></div></div>
  <div class="card" style="left:411px;top:261px"><div class="img" role="img" aria-label="Produktfoto: grüne Longboard-Rollen" style="background:radial-gradient(ellipse 45% 32% at 50% 45%,#46e23e,#fff)"></div><div class="nm"><a>RONDO</a> | à 10,50 €</div><p>Lorem Ipsum. Proin gravidanv<br>el velit auctor aliquet... <a>mehr</a></p><div class="btns"><span class="d">DETAILS</span><span class="w">IN DEN WARENKORB</span></div></div>
</section>
<div class="abs pg" style="left:659px"><svg width="12" height="10" viewBox="0 0 12 10"><path d="M5.5 1L1.5 5l4 4M10.5 1l-4 4 4 4" fill="none" stroke="#222" stroke-width="2"/></svg></div>
<div class="abs pg" style="left:697px"><svg width="12" height="10" viewBox="0 0 12 10"><path d="M1.5 1l4 4-4 4M6.5 1l4 4-4 4" fill="none" stroke="#1a95c4" stroke-width="2"/></svg></div>

<footer class="abs foot">
  <div class="col" style="left:240px">
    <h4><span>BRETTMARKT.DE</span> TAGS</h4>
    <div class="tags">
      <div class="row"><span>Griptape</span><span class="on">Skate-Tools</span><span>Trucks</span></div>
      <div class="row"><span>Wachs</span><span>MRVK</span><span>Orbis</span><span>KUGEL7</span></div>
      <div class="row"><span>Helme</span><span>Schoner</span><span>Hafenviertel</span><span>Zenitra</span></div>
      <div class="row"><span>Lenkgummi</span><span>Kingpin</span><span>Brenner</span><span style="background:none">etc.</span></div>
    </div>
  </div>
  <div class="col" style="left:454px">
    <h4><span>BRETTMARKT.DE</span> KONTAKT</h4>
    <div style="display:flex;gap:26px;margin-top:14px;line-height:15.5px">
      <div><b style="font-weight:600">brettmarkt.de</b><br>Brettweg 1<br>10000 Rollstadt<br>Deutschland</div>
      <div>T: 10000 - 11 22 33 44 55<br>F: 10000 - 11 22 33 44 56<br>M: <a>info@brettmarkt.de</a><br>W: <a>www.brettmarkt.de</a></div>
    </div>
  </div>
  <div class="col" style="left:750px;width:210px">
    <h4><span>BRETTMARKT.DE</span> VERSANDINFOS</h4>
    <p style="margin-top:14px;line-height:15.5px;text-align:justify">Nationaler und internationaler Versand. Die folgenden Zahlungsmethoden werden akzeptiert:</p>
    <div class="pay"><span>Zahlfix</span><span>Kartenmeister</span><span>Vistra</span><span>Ameroxa</span></div>
    <p style="margin-top:6px">Weitere Details finden Sie <a>hier</a>.</p>
  </div>
</footer>
<div class="abs copy">Copyright © 2013 brettmarkt.de &nbsp;|&nbsp; Alle Rechte vorbehalten.</div>
</body>
</html>
```